Ein gutes einfühlen in mich als Kunde, viel Eigeninitiative und zügiges arbeiten, ich bin sehr zufrieden!
Zielgruppe
Ich bin Coach und führe Gespräche mit Frauen die durch die Situation im Aussen oder Lebensümstände überlastet oder überfordert sind.
Aufgabenstellung
Ich mag ein klares und gleichzeitig liebevoll Frauen einladendes Design. Ich mag kein blau und grau dafür aber warme und natürliche Farben.
Ich brauche auch noch einen doppelseitigen Hochkantflyer
Der Text ist: Gespräche zu zweit - für Seelentrost und innere Harmonie (das ist die erste Idee)

```html
<!DOCTYPE html>
<html lang="de">
<head>
<meta charset="utf-8">
<title>Visitenkarte – Liesbeth Krommhoof, Coach</title>
<link rel="stylesheet" href="https://fonts.googleapis.com/css2?family=Space+Mono&family=Archivo:wght@400;700&display=swap">
<style>
  :root {
    --page: #ffffff;
    --terracotta: #b06f5c;
    --rose-clay: #c98f7d;
    --blush: #f3dcd2;
    --apricot: #ddb39c;
    --line-sand: #f6e2cf;
    --cream: #f8f3ea;
    --ink-earth: #8c5443;
    --ink-earth-light: #a36e5c;
    --text-light: #fff8f2;
  }
  * { margin: 0; padding: 0; box-sizing: border-box; }
  html, body {
    width: 905px; height: 1200px; overflow: hidden;
    background: var(--page);
  }
  .sheet { position: relative; width: 905px; height: 1200px; }

  .card {
    position: absolute; left: 39px; width: 828px; overflow: hidden;
  }
  .card--front {
    top: 21px; height: 473px;
    background: linear-gradient(100deg, var(--terracotta), var(--rose-clay) 60%, var(--terracotta));
  }
  .card--back { top: 678px; height: 471px; background: var(--cream); }

  .card__shapes { position: absolute; inset: 0; width: 100%; height: 100%; }

  .front__panel {
    position: absolute; left: 62px; top: 51px; width: 560px; height: 422px;
    background: linear-gradient(90deg, var(--blush) 0%, var(--apricot) 45%, rgba(201,143,125,0) 100%);
  }
  .front__tagline {
    position: absolute; left: 94px; top: 199px;
    font-family: "Space Mono", monospace;
    font-size: 29px; line-height: 52px; letter-spacing: 8px;
    color: var(--text-light);
    white-space: nowrap;
  }

  .name-box {
    position: absolute; left: 47px; top: 154px; width: 270px; height: 163px;
    border: 1.5px solid var(--ink-earth-light);
    padding: 28px 0 0 21px;
    font-family: "Archivo", sans-serif;
    color: var(--ink-earth);
  }
  .name-box__name {
    font-weight: 700; font-size: 29px; line-height: 33px; letter-spacing: 0.3px;
  }
  .name-box__role {
    margin-top: 14px; font-size: 20px; color: var(--ink-earth-light);
  }

  .contact {
    position: absolute; left: 428px; top: 112px;
    font-family: "Space Mono", monospace;
    font-size: 18px; letter-spacing: 1.4px;
    color: var(--ink-earth-light); font-style: normal;
    white-space: nowrap;
  }
  .contact__address { line-height: 37px; }
  .contact__mail { margin-top: 48px; }
  .contact__web { margin-top: 81px; }
</style>
</head>
<body>
<main class="sheet">

  <section class="card card--front" aria-label="Vorderseite">
    <svg class="card__shapes" viewBox="0 0 828 473" aria-hidden="true">
      <defs>
        <linearGradient id="orbFront" x1="0" y1="0" x2="1" y2="1">
          <stop offset="0" stop-color="#cf9a86"/>
          <stop offset="1" stop-color="#a9654f"/>
        </linearGradient>
      </defs>
      <circle cx="370" cy="-10" r="104" fill="#c88d79" opacity="0.7"/>
      <circle cx="702" cy="92" r="131" fill="url(#orbFront)"/>
      <circle cx="787" cy="336" r="85" fill="url(#orbFront)"/>
    </svg>
    <div class="front__panel"></div>
    <svg class="card__shapes" viewBox="0 0 828 473" aria-hidden="true">
      <defs>
        <linearGradient id="orbLow" x1="1" y1="0" x2="0" y2="1">
          <stop offset="0" stop-color="#cf9a86"/>
          <stop offset="1" stop-color="#b06f5c"/>
        </linearGradient>
      </defs>
      <circle cx="148" cy="471" r="109" fill="url(#orbLow)"/>
      <g stroke="var(--line-sand)" stroke-width="1.6" fill="none">
        <line x1="646" y1="2" x2="772" y2="130"/>
        <line x1="524" y1="342" x2="655" y2="471"/>
        <line x1="764" y1="308" x2="828" y2="370"/>
      </g>
    </svg>
    <p class="front__tagline">Gespräche zu zweit – für<br>Seelentrost und innere<br>Harmonie</p>
  </section>

  <section class="card card--back" aria-label="Rückseite">
    <svg class="card__shapes" viewBox="0 0 828 471" aria-hidden="true">
      <defs>
        <linearGradient id="orbSand" x1="0" y1="0" x2="1" y2="0.6">
          <stop offset="0" stop-color="#f8f3ea"/>
          <stop offset="1" stop-color="#efd9c6"/>
        </linearGradient>
        <linearGradient id="orbBlush" x1="0" y1="0" x2="1" y2="1">
          <stop offset="0" stop-color="#f8f3ea"/>
          <stop offset="1" stop-color="#f5e1da"/>
        </linearGradient>
        <linearGradient id="orbBlushLow" x1="1" y1="1" x2="0" y2="0">
          <stop offset="0" stop-color="#f8f3ea"/>
          <stop offset="1" stop-color="#f4ddd5"/>
        </linearGradient>
      </defs>
      <circle cx="345" cy="-58" r="94" fill="url(#orbSand)"/>
      <circle cx="730" cy="92" r="122" fill="url(#orbBlush)"/>
      <circle cx="148" cy="449" r="109" fill="url(#orbBlushLow)"/>
      <circle cx="627" cy="477" r="94" fill="url(#orbSand)"/>
    </svg>

    <div class="name-box">
      <h1 class="name-box__name">LIESBETH<br>KROMMHOOF</h1>
      <p class="name-box__role">Coach</p>
    </div>

    <address class="contact">
      <p class="contact__address">Rosengarten 7, 54321<br>Lindenau</p>
      <p class="contact__mail">hallo@liesbeth-gespraeche.de</p>
      <p class="contact__web">www.liesbeth-gespraeche.de</p>
    </address>
  </section>

</main>
</body>
</html>
```